Poster design for a company operating care homes in the UK showcasing our core values

We need a poster to display in our care homes showcasing our new core values:

Purpose
We are driven by a clear understanding of why we do what we do: to enrich lives, honour legacies and make a meaningful difference every day, for our residents, their families, our colleagues and our community.

Excellence
We hold ourselves to the highest standards, delivering exceptional care and creating an environment where both residents and staff can thrive.

Openness
We build trust through honest, respectful communication, welcoming feedback, sharing ideas, and embracing change as a path to continuous growth.

Passion
We are passionate about delivering exceptional care. We take pride in what we do and in making a real difference in people’s lives.

Learning
We are committed to personal and professional growth; empowering each other through ongoing development, reflection, and shared knowledge.

Empathy
We actively listen and seek to understand before being understood, recognising the unique stories, feelings, and needs of others.

I have attached a small graphic that we would like you try to incorporate, in addition to our company logo. Please theme the rest of the poster around our company colours.

```html
<!DOCTYPE html>
<html lang="en">
<head>
<meta charset="utf-8">
<title>Corvale – Our Core Values</title>
<link rel="stylesheet" href="https://fonts.googleapis.com/css2?family=Montserrat:wght@500;600&display=swap">
<style>
  :root {
    --navy: #0f2259;
    --slate: #3a5070;
    --peach: #f3c4a9;
    --peach-deep: #eea98a;
    --paper: #f8f6f4;
    --white: #ffffff;
  }
  * { margin: 0; padding: 0; box-sizing: border-box; }
  html, body { width: 821px; height: 1200px; overflow: hidden; background: var(--paper); }
  .poster {
    position: relative;
    width: 821px;
    height: 1200px;
    overflow: hidden;
    background: var(--paper);
    font-family: "Montserrat", Arial, sans-serif;
  }
  .backdrop { position: absolute; inset: 0; }
  .brand-panel {
    position: absolute;
    left: 132px; top: 56px;
    width: 584px; height: 163px;
    background: var(--white);
    display: flex;
    flex-direction: column;
    align-items: center;
    justify-content: center;
    gap: 12px;
  }
  .brand-name {
    display: flex;
    align-items: center;
    gap: 18px;
    font-weight: 600;
    font-size: 62px;
    letter-spacing: 1px;
    color: var(--slate);
    line-height: 1;
  }
  .brand-mark { width: 40px; height: 40px; background: var(--slate); }
  .brand-tagline {
    font-weight: 500;
    font-size: 19px;
    letter-spacing: 3px;
    color: var(--slate);
  }
  .values-graphic {
    position: absolute;
    left: 63px; top: 280px;
    width: 695px; height: 178px;
    border-radius: 24px;
    background: linear-gradient(90deg, var(--peach) 0%, #8d8aa0 50%, var(--navy) 100%);
  }
  .value {
    position: absolute;
    width: 186px;
    color: var(--white);
  }
  .value h2 {
    font-weight: 500;
    font-size: 31px;
    color: var(--peach-deep);
    margin-bottom: 20px;
    line-height: 1;
  }
  .value p {
    font-weight: 600;
    font-size: 14.6px;
    line-height: 17.9px;
  }
</style>
</head>
<body>
<main class="poster">
  <svg class="backdrop" width="821" height="1200" viewBox="0 0 821 1200" aria-hidden="true">
    <path d="M0,520 C200,500 420,600 821,530 L821,1200 L0,1200 Z" fill="var(--navy)"/>
    <path d="M0,505 C200,485 420,585 821,515" fill="none" stroke="var(--peach)" stroke-width="1.5"/>
  </svg>

  <header class="brand-panel">
    <div class="brand-name"><span class="brand-mark"></span>CORVALE</div>
    <div class="brand-tagline">Caring Together</div>
  </header>

  <div class="values-graphic" role="img" aria-label="Values graphic spelling PEOPLE from Purpose, Excellence, Openness, Passion, Learning and Empathy"></div>

  <section class="value" style="left:86px; top:655px;">
    <h2>Purpose-</h2>
    <p>We are driven by a clear understanding of why we do what we do: to enrich lives, honour legacies and make a meaningful difference every day, for our residents, their families, our colleagues and our community.</p>
  </section>
  <section class="value" style="left:331px; top:655px;">
    <h2>Excellence-</h2>
    <p>We hold ourselves to the highest standards, delivering exceptional care and creating an environment where both residents and staff can thrive.</p>
  </section>
  <section class="value" style="left:577px; top:655px;">
    <h2>Openness-</h2>
    <p>We build trust through honest, respectful communication, welcoming feedback, sharing ideas, and embracing change as a path to continuous growth.</p>
  </section>
  <section class="value" style="left:91px; top:921px;">
    <h2>Passion-</h2>
    <p>We are passionate about delivering exceptional care. We take pride in what we do and in making a real difference in people’s lives.</p>
  </section>
  <section class="value" style="left:331px; top:921px;">
    <h2>Learning-</h2>
    <p>We are committed to personal and professional growth; empowering each other through ongoing development, reflection, and shared knowledge.</p>
  </section>
  <section class="value" style="left:571px; top:921px;">
    <h2>Empathy-</h2>
    <p>We actively listen and seek to understand before being understood, recognising the unique stories, feelings, and needs of others.</p>
  </section>
</main>
</body>
</html>
```